Personal Biography Website for a Professional Game Developer

I'm looking for someone to design a personal biography website for a professional game developer. Look at the attached logos, headshots, and art as examples of the type of style that I'm looking for. This should be an edgy, progressive-style website -- like one you'd expect from a video game website.
I'm also a huge fan of the brelt website... large images for each section with little text.
I've attached the bio text as well (the underlines are just place holders)
Target Market(s)
Venture Capital, Video Game Developers
Number of Pages Required
1 page
Look and feel
Each slider illustrates characteristics of the customer's brand and the style your logo design should communicate.

```html
<!DOCTYPE html>
<html lang="en">
<head>
<meta charset="utf-8">
<title>Dario Costel — Game Developer</title>
<link rel="stylesheet" href="https://fonts.googleapis.com/css2?family=Montserrat:wght@500;600;700;800;900&family=Open+Sans:wght@400;600;700&display=swap">
<style>
:root{
  --red:#e3262e;
  --blue:#3ea7d8;
  --purple:#7a3bb0;
  --ink:#0b0b0c;
  --panel:#151516;
  --line:#2a2a2c;
  --white:#ffffff;
  --muted:#b9b9bd;
  --head:'Montserrat',Arial,sans-serif;
  --body:'Open Sans',Arial,sans-serif;
}
*{box-sizing:border-box;margin:0;padding:0}
html,body{width:1200px;height:4000px;overflow:hidden;background:var(--ink);color:var(--white);font-family:var(--body)}
.page{position:relative;width:1200px;height:4000px}
section,header,footer{position:absolute;left:0;width:1200px}
.btn{position:absolute;display:flex;align-items:center;justify-content:center;border-radius:30px;font-family:var(--head);font-weight:800;font-size:15px;letter-spacing:.5px;color:var(--white)}
.btn-gradient{background:linear-gradient(90deg,var(--blue),var(--red))}
.section-title{position:absolute;left:0;width:1200px;text-align:center;font-family:var(--head);font-weight:900;font-size:60px;letter-spacing:2px}

/* brand */
.brand{position:absolute;display:flex;align-items:center;gap:10px;font-family:var(--head);font-weight:800;font-size:28px;color:var(--white)}
.brand .mark{width:16px;height:16px;background:var(--red)}

/* hero */
.hero{top:0;height:660px;background:linear-gradient(90deg,#060607 0%,#0d0d10 55%,#111 100%)}
.hero .brand{left:90px;top:48px}
.nav{position:absolute;right:80px;top:52px;display:flex;gap:26px;font-family:var(--head);font-weight:700;font-size:15px}
.nav a{color:var(--white);text-decoration:none}
.nav a.active{color:var(--red)}
.hero-photo{position:absolute;left:720px;top:0;width:440px;height:660px;background:radial-gradient(ellipse at 45% 40%,#5a1434 0%,#1e0b24 45%,#0a0a10 80%)}
.hero-welcome{position:absolute;left:100px;top:270px;font-family:var(--head);font-weight:900;font-size:42px;background:linear-gradient(90deg,var(--purple),#c03a7a);-webkit-background-clip:text;background-clip:text;color:transparent}
.hero-name{position:absolute;left:100px;top:330px;font-family:var(--head);font-weight:900;font-size:46px;letter-spacing:1px}
.hero-role{position:absolute;left:100px;top:405px;font-family:var(--head);font-weight:800;font-size:26px;color:var(--red)}
.hero .btn{top:480px;height:40px;width:120px;font-size:13px}
.btn-work{left:100px;border:3px solid var(--blue)}
.btn-hire{left:240px;border:3px solid var(--red)}

/* intro */
.intro{top:680px;height:700px;background:var(--panel)}
.intro-frame{position:absolute;left:130px;top:110px;width:470px;height:520px;border-left:10px solid var(--blue);border-bottom:10px solid var(--red)}
.intro-photo{position:absolute;left:150px;top:110px;width:450px;height:500px;background:linear-gradient(135deg,#dcdcdc,#5a5a5a 55%,#151515)}
.intro-kicker{position:absolute;left:645px;top:108px;font-family:var(--head);font-weight:500;font-size:22px;letter-spacing:1px}
.intro-title{position:absolute;left:645px;top:136px;font-family:var(--head);font-weight:900;font-size:58px;color:var(--red);letter-spacing:2px}
.intro-text{position:absolute;left:645px;top:225px;width:460px;font-size:15px;line-height:23px;color:var(--muted)}
.intro .btn{top:592px;height:50px}
.btn-cv{left:645px;width:180px}
.btn-more{left:850px;width:160px;border:3px solid var(--white);background:var(--ink)}

/* services */
.services{top:1380px;height:580px;background:var(--ink)}
.services .section-title{top:60px}
.service{position:absolute;top:210px;width:300px;height:220px;border:1px solid #cfcfd2;padding:44px 22px 0}
.service h3{text-align:center;font-family:var(--head);font-weight:800;font-size:17px;margin-bottom:12px}
.service p{text-align:center;font-size:12px;line-height:18px;color:var(--muted)}
.service-icon{position:absolute;left:115px;top:-45px;width:70px;height:70px;display:flex;align-items:center;justify-content:center}
.service.c1{left:100px}.service.c2{left:450px}.service.c3{left:800px}
.service.c1 h3,.service.c3 h3{color:var(--red)}
.service.c2 h3{color:var(--blue)}
.service.c1 .service-icon,.service.c3 .service-icon{background:var(--blue)}
.service.c2 .service-icon{background:var(--red)}
.services .btn{left:520px;top:480px;width:160px;height:48px}

/* portfolio */
.portfolio{top:1960px;height:660px;background:var(--panel)}
.portfolio .section-title{top:60px}
.work{position:absolute;top:188px;width:225px;height:300px;background:#0f0f10;border:1px solid var(--line)}
.work-img{height:180px}
.work-meta{display:flex;justify-content:space-between;padding:12px 14px 0;font-size:11px;font-family:var(--head);font-weight:700}
.work-meta .cat{color:var(--red)}
.work-meta .count{color:var(--blue)}
.work h4{padding:10px 14px 0;font-family:var(--head);font-weight:800;font-size:18px;line-height:23px}
.w1{left:108px}.w2{left:360px}.w3{left:612px}.w4{left:864px}
.w1 .work-img{background:linear-gradient(160deg,#9fb7c8,#2c4a63 60%,#0f1b27)}
.w2 .work-img{background:linear-gradient(160deg,#5a2a6e,#c2346a 55%,#2a0f24)}
.w3 .work-img{background:linear-gradient(160deg,#2b1a14,#a8442a 55%,#1a0d0a)}
.w4 .work-img{background:linear-gradient(160deg,#2d3a8a,#b8345a 60%,#1a1030)}
.portfolio .btn{left:520px;top:570px;width:160px;height:48px}

/* releases */
.releases{top:2620px;height:680px;background:var(--ink)}
.releases .section-title{top:60px}
.arrows{position:absolute;left:955px;top:82px;display:flex;align-items:center;gap:10px}
.arrows .arr{width:30px;height:30px;display:flex;align-items:center;justify-content:center;background:#2a2a2c}
.arrows .arr.next{background:var(--red)}
.arrows .bar{width:60px;height:3px;background:#555}
.release{position:absolute;top:185px;width:270px;height:430px;background:#111;overflow:hidden}
.release-img{height:280px;position:relative}
.release-tag{position:absolute;right:0;top:0;padding:8px 12px;background:#0b0b0c;font-family:var(--head);font-weight:800;font-size:13px;color:var(--white)}
.release-body{height:150px;padding:20px 16px 0;text-align:center}
.release-body h4{font-family:var(--head);font-weight:900;font-size:19px}
.release-body p{font-size:12px;line-height:17px;margin:6px 0 10px}
.release-body .view{display:inline-block;background:#fff;color:#111;font-family:var(--head);font-weight:800;font-size:12px;padding:5px 18px}
.r1{left:165px}.r2{left:465px}.r3{left:800px}
.r1 .release-img{background:linear-gradient(160deg,#e98a6a,#7a3a3a 55%,#2a1a22)}
.r2 .release-img{background:linear-gradient(180deg,#7fd6e8,#3fa9c8 45%,#c8402e 85%)}
.r3 .release-img{background:linear-gradient(180deg,#5c6f8a,#2b3a52 60%,#121a28)}
.r1 .release-body,.r3 .release-body{background:var(--blue)}
.r2 .release-body{background:var(--red)}

/* newsletter */
.newsletter{top:3300px;height:300px;background:var(--panel)}
.newsletter h2{position:absolute;left:100px;top:70px;font-family:var(--head);font-weight:900;font-size:46px}
.newsletter p{position:absolute;left:100px;top:150px;width:480px;font-size:16px;line-height:24px;color:var(--muted)}
.nl-input{position:absolute;left:605px;top:152px;width:340px;height:54px;border:2px solid #d0d0d0;display:flex;align-items:center;padding-left:20px;font-size:15px;color:#ddd}
.newsletter .btn{left:970px;top:152px;width:150px;height:54px;font-size:17px}

/* footer */
.footer{top:3600px;height:340px;background:var(--ink)}
.footer .brand{left:90px;top:110px;font-size:30px}
.contact{position:absolute;top:85px;width:260px}
.contact h5{display:flex;align-items:center;gap:12px;font-family:var(--head);font-weight:800;font-size:20px;letter-spacing:1px;margin-bottom:18px}
.contact p{padding-left:40px;font-size:14px;line-height:22px;color:var(--muted)}
.ct1{left:350px}.ct2{left:640px}.ct3{left:920px}
.copyright{top:3940px;height:60px;background:#050505;border-top:1px solid var(--line)}
.copyright small{position:absolute;left:90px;top:22px;font-size:13px;color:var(--muted)}
.social{position:absolute;right:90px;top:10px;display:flex;gap:16px}
.social span{width:40px;height:40px;border-radius:50%;background:var(--red)}
</style>
</head>
<body>
<div class="page">

<header class="hero">
  <div class="hero-photo" role="img" aria-label="Portrait of the developer lit in red and blue"></div>
  <div class="brand"><span class="mark"></span>Costelworks</div>
  <nav class="nav">
    <a class="active">HOME</a><a>ABOUT ME</a><a>OUR GAMES</a><a>WORK</a><a>BLOG</a><a>CONTACT</a>
  </nav>
  <div class="hero-welcome">WELCOME! I'M</div>
  <h1 class="hero-name">DARIO COSTEL</h1>
  <div class="hero-role">GAME DEVELOPER</div>
  <a class="btn btn-work">MY WORK</a>
  <a class="btn btn-hire">HIRE ME</a>
</header>

<section class="intro">
  <div class="intro-frame"></div>
  <div class="intro-photo" role="img" aria-label="Black and white portrait of the developer"></div>
  <div class="intro-kicker">INTRODUCING</div>
  <h2 class="intro-title">MYSELF</h2>
  <p class="intro-text">Establishing my services on a foundation of integrity, I am a highly dynamic Engineering Executive who has been passionately accelerating the gaming/entertainment experience for the last 13+ years. Being a professional fueled by mission excellence, I hold a rich history of working with illustrious corporations, including (but not limited to) Brimstone Games, Learnwave, and KTSG. Entrepreneur along with freelance gaming development, and have ultimately built a strong reputation for driving new levels of gaming success and overall team unification (born and raised into a family of software developers). It ended up becoming the catalyst for me to follow the same path regardless of my early reservations about doing so.</p>
  <a class="btn btn-gradient btn-cv">DOWNLOAD CV</a>
  <a class="btn btn-more">READ MORE</a>
</section>

<section class="services">
  <h2 class="section-title">WHAT I DO?</h2>
  <div class="service c1">
    <div class="service-icon"><svg width="44" height="30" viewBox="0 0 44 30"><rect x="2" y="4" width="40" height="22" rx="11" fill="#fff"/><rect x="10" y="13" width="10" height="3" fill="#3ea7d8"/><rect x="13.5" y="9.5" width="3" height="10" fill="#3ea7d8"/><circle cx="30" cy="12" r="2.2" fill="#3ea7d8"/><circle cx="34" cy="17" r="2.2" fill="#3ea7d8"/></svg></div>
    <h3>GAME DEVELOPING</h3>
    <p>As a dynamic creative within gaming technology I have a genuine passion for translating creative blueprints into tangible realities and doing so while ensuring everyone involved has positive constructive experiences along the way.</p>
  </div>
  <div class="service c2">
    <div class="service-icon"><svg width="44" height="30" viewBox="0 0 44 30"><rect x="2" y="4" width="40" height="22" rx="11" fill="#fff"/><rect x="10" y="13" width="10" height="3" fill="#e3262e"/><rect x="13.5" y="9.5" width="3" height="10" fill="#e3262e"/><circle cx="30" cy="12" r="2.2" fill="#e3262e"/><circle cx="34" cy="17" r="2.2" fill="#e3262e"/></svg></div>
    <h3>GAME DEVELOPING</h3>
    <p>As a dynamic creative within gaming technology I have a genuine passion for translating creative blueprints into tangible realities and doing so while ensuring everyone involved has positive constructive experiences along the way.</p>
  </div>
  <div class="service c3">
    <div class="service-icon"><svg width="44" height="30" viewBox="0 0 44 30"><rect x="2" y="4" width="40" height="22" rx="11" fill="#fff"/><rect x="10" y="13" width="10" height="3" fill="#3ea7d8"/><rect x="13.5" y="9.5" width="3" height="10" fill="#3ea7d8"/><circle cx="30" cy="12" r="2.2" fill="#3ea7d8"/><circle cx="34" cy="17" r="2.2" fill="#3ea7d8"/></svg></div>
    <h3>GAME DEVELOPING</h3>
    <p>As a dynamic creative within gaming technology I have a genuine passion for translating creative blueprints into tangible realities and doing so while ensuring everyone involved has positive constructive experiences along the way.</p>
  </div>
  <a class="btn btn-gradient">VIEW MORE</a>
</section>

<section class="portfolio">
  <h2 class="section-title">MY PORTFILO</h2>
  <article class="work w1"><div class="work-img" role="img" aria-label="Game artwork of a snowy landscape"></div><div class="work-meta"><span class="cat">DEVELOPMENT</span><span class="count">136</span></div><h4>MOBILE APP FOR GAMING</h4></article>
  <article class="work w2"><div class="work-img" role="img" aria-label="Gamer playing in neon-lit room"></div><div class="work-meta"><span class="cat">DEVELOPMENT</span><span class="count">136</span></div><h4>MOBILE APP FOR GAMING</h4></article>
  <article class="work w3"><div class="work-img" role="img" aria-label="Gaming setup with glowing screens"></div><div class="work-meta"><span class="cat">DEVELOPMENT</span><span class="count">136</span></div><h4>MOBILE APP FOR GAMING</h4></article>
  <article class="work w4"><div class="work-img" role="img" aria-label="Player with headset in colourful light"></div><div class="work-meta"><span class="cat">DEVELOPMENT</span><span class="count">136</span></div><h4>MOBILE APP FOR GAMING</h4></article>
  <a class="btn btn-gradient">VIEW MORE</a>
</section>

<section class="releases">
  <h2 class="section-title">LATEST RELEASES</h2>
  <div class="arrows">
    <span class="arr"><svg width="12" height="12" viewBox="0 0 12 12"><path d="M8 1 3 6l5 5" stroke="#fff" stroke-width="2" fill="none"/></svg></span>
    <span class="bar"></span>
    <span class="arr next"><svg width="12" height="12" viewBox="0 0 12 12"><path d="M4 1l5 5-5 5" stroke="#fff" stroke-width="2" fill="none"/></svg></span>
  </div>
  <article class="release r1"><div class="release-img" role="img" aria-label="Game art of a character in a sunset city"><span class="release-tag">Costelworks</span></div><div class="release-body"><h4>LOREM IPSUM</h4><p>Lorem ipsum dolor sit amet, consectetur adipiscing elit sed do.</p><span class="view">VIEW GAME</span></div></article>
  <article class="release r2"><div class="release-img" role="img" aria-label="Game art of a red car on a tropical road"><span class="release-tag">Costelworks</span></div><div class="release-body"><h4>LOREM IPSUM</h4><p>Lorem ipsum dolor sit amet, consectetur adipiscing elit sed do.</p><span class="view">VIEW GAME</span></div></article>
  <article class="release r3"><div class="release-img" role="img" aria-label="Game art of a misty futuristic landscape"><span class="release-tag">Costelworks</span></div><div class="release-body"><h4>LOREM IPSUM</h4><p>Lorem ipsum dolor sit amet, consectetur adipiscing elit sed do.</p><span class="view">VIEW GAME</span></div></article>
</section>

<section class="newsletter">
  <h2>OUR NEWSLETTER</h2>
  <p>Sign up for our e-mail newsletter and stay informed for what's next on horizon</p>
  <div class="nl-input">Your e-mail address</div>
  <a class="btn btn-gradient">SIGN UP</a>
</section>

<footer class="footer">
  <div class="brand"><span class="mark"></span>Costelworks</div>
  <div class="contact ct1">
    <h5><svg width="26" height="30" viewBox="0 0 26 30"><path d="M13 29C5 19 3 15 3 11a10 10 0 0 1 20 0c0 4-2 8-10 18z" fill="#e3262e"/><circle cx="13" cy="11" r="4" fill="#0b0b0c"/></svg>LOCATION</h5>
    <p>123 Ipsum dolor sit consectetur adipiscing magna aliqua.</p>
  </div>
  <div class="contact ct2">
    <h5><svg width="28" height="22" viewBox="0 0 28 22"><rect x="1" y="1" width="26" height="20" fill="#e3262e"/><path d="M1 1l13 11L27 1" stroke="#0b0b0c" stroke-width="2" fill="none"/></svg>E-MAIL ME</h5>
    <p>hello@costelworks.com</p>
  </div>
  <div class="contact ct3">
    <h5><svg width="28" height="22" viewBox="0 0 28 22"><rect x="1" y="1" width="26" height="20" fill="#e3262e"/><path d="M1 1l13 11L27 1" stroke="#0b0b0c" stroke-width="2" fill="none"/></svg>CALL ME</h5>
    <p>+1 555 014 2290</p>
  </div>
</footer>

<section class="copyright">
  <small>COPYRIGHT © 2022 DARIO COSTEL</small>
  <div class="social"><span></span><span></span><span></span></div>
</section>

</div>
</body>
</html>
```